Cobalt Skyway is an innovative offering which enables the mass market to book seats on private jets at commercial airline prices to destinations worldwide.

We need a lgog and Wordpress theme header for this initiative. Will like need other matrials but need these two images asap

Industry/Entity Type

Social

```html
<!DOCTYPE html>
<html lang="en">
<head>
<meta charset="utf-8">
<title>Cobalt Skyway</title>
<link href="https://fonts.googleapis.com/css2?family=Cinzel:wght@400;600&family=Arimo:wght@400;700&family=Tinos&display=swap" rel="stylesheet">
<style>
:root{
  --black:#000;
  --slate:#4b5566;
  --slate-dark:#1d232c;
  --panel:#2a313c;
  --rule:#5a616b;
  --text:#ffffff;
  --muted:#9aa0aa;
  --accent:#6f9fc4;
  --field:#0d0f12;
  --field-line:#6a7079;
  --btn:#1a1c20;
  --sky-top:#7d9bbd;
  --sky-bottom:#b7c7d8;
}
*{margin:0;padding:0;box-sizing:border-box}
html,body{width:1200px;height:876px;overflow:hidden;background:var(--black)}
body{position:relative;font-family:"Arimo",Arial,sans-serif;color:var(--text)}
.abs{position:absolute}
.top-strip{left:0;top:106px;width:158px;height:8px;background:linear-gradient(90deg,#1a1d22,#5d6470 70%,#2b2f36)}
.header-band{left:374px;top:0;width:826px;height:94px;background:linear-gradient(90deg,#4f5a6b 0%,#3a4250 55%,#0d0f13 100%)}
.brand{left:158px;top:0;width:216px;height:114px;background:linear-gradient(180deg,#7a8697 0%,#55606f 55%,#2b323d 100%);text-align:center}
.brand-name{display:block;margin-top:26px;font-family:"Cinzel",serif;font-weight:600;font-size:24px;color:#fff;letter-spacing:.5px}
.brand-mark{display:block;width:10px;height:10px;border-radius:50%;background:#fff;margin:12px auto 0}
.phone{right:156px;top:32px;font-family:"Cinzel",serif;font-size:18px;color:#fff}
.nav{left:374px;top:94px;width:826px;height:20px;background:linear-gradient(90deg,#2a303a,#161a20);display:flex;align-items:center;padding-left:7px;font-family:"Tinos",serif;font-size:13px}
.nav a{color:#fff;text-decoration:none}
.nav .dot{width:4px;height:4px;background:#6f8cae;margin:0 20px}
.sidebar{left:158px;top:114px;width:216px;height:508px;background:linear-gradient(180deg,#1e242d 0%,#2b323c 55%,#161a20 100%)}
.planner-title{left:172px;top:139px;font-family:"Cinzel",serif;font-size:16px;color:#7fa3c4}
.trip{left:182px;top:202px;display:flex;gap:20px;font-size:11px;font-weight:700}
.trip span{display:flex;align-items:center;gap:5px}
.radio{width:10px;height:10px;border-radius:50%;background:#ddd;border:2px solid #ccc}
.radio.on{background:#7ac46e;border-color:#e8e8e8}
.label{font-size:11px;font-weight:700}
.field{height:19px;background:var(--field);border:1px solid var(--field-line);font-size:11px;color:#888;padding:2px 3px;line-height:13px}
.select{height:19px;background:#000;border:1px solid var(--field-line);font-size:11px;padding:2px 3px;display:flex;justify-content:space-between}
.select i{width:16px;height:17px;margin:-2px -3px 0 0;background:linear-gradient(#d9e3f2,#9fb4d4);display:flex;align-items:center;justify-content:center}
.btn-question{left:172px;top:469px;width:108px;height:23px;border-radius:4px;background:linear-gradient(#7e9dc4,#3b5a85);border:1px solid #9cb3d0;font-family:"Cinzel",serif;font-size:12px;text-align:center;line-height:21px}
.btn-go{left:286px;top:468px;width:48px;height:24px;border-radius:5px;background:linear-gradient(#3a3d42,#0c0d0f);border:1px solid #555;font-family:"Tinos",serif;font-size:14px;text-align:center;line-height:22px}
.contact-card{left:163px;top:508px;width:171px;height:66px;background:linear-gradient(90deg,#8a6b55 0%,#c9c2bb 45%,#eeeeee 100%)}
.contact-card span{position:absolute;right:4px;top:22px;font-family:"Tinos",serif;font-size:18px;color:#111}
.hero{left:374px;top:127px;width:649px;height:276px;background:linear-gradient(180deg,var(--sky-top) 0%,#9fb6cf 50%,var(--sky-bottom) 100%)}
.hero-band{left:374px;top:314px;width:348px;height:72px;background:linear-gradient(90deg,rgba(90,100,120,.85),rgba(90,100,120,0))}
.hero-title{left:406px;top:336px;font-family:"Cinzel",serif;font-size:21px;letter-spacing:1.5px}
.divider{left:0;top:412px;width:1200px;height:1px;background:var(--rule)}
.content{left:374px;top:413px;width:826px;height:230px;background:radial-gradient(ellipse 60% 90% at 45% 10%,#59616d 0%,#373e48 45%,rgba(0,0,0,0) 100%)}
.col-head{font-family:"Cinzel",serif;font-size:13px;border-bottom:1px solid #8a9099;padding-bottom:1px;width:194px}
.quote{font-size:10.5px;line-height:17.5px;width:185px}
.vline{left:585px;top:463px;width:1px;height:110px;background:#5c636d}
.pill{height:20px;border-radius:10px;background:linear-gradient(#3b3e44,#111);border:1px solid #555;font-family:"Cinzel",serif;font-size:10px;line-height:18px;text-align:center}
.signature{left:525px;top:594px;font-size:11px;font-weight:700;color:var(--accent)}
.video-link{left:634px;top:590px;font-size:10.5px;color:#fff;text-decoration:underline}
.gallery{left:822px;top:457px;width:181px;height:97px;background:linear-gradient(180deg,#1d4f8c,#0f2d57)}
.social{top:682px;display:flex;gap:14px;left:870px;font-size:11px;color:var(--muted)}
.countries{left:0;width:1168px;text-align:center;font-size:11.5px;color:var(--muted);line-height:23px;top:741px}
.copy{left:0;width:1168px;text-align:center;top:828px;font-size:11px;color:var(--muted)}
</style>
</head>
<body>
<div class="abs top-strip"></div>
<div class="abs header-band"></div>
<div class="abs brand"><span class="brand-name">COBALT SKYWAY</span><span class="brand-mark"></span></div>
<div class="abs phone">CALL US: 555-240-7788</div>
<nav class="abs nav">
  <a>The Experience</a><span class="dot"></span><a>Why Cobalt Skyway?</a><span class="dot"></span><a>Air Safety</a><span class="dot"></span><a>Aircraft Clients</a><span class="dot"></span><a>News</a><span class="dot"></span><a>Contact US</a>
</nav>

<aside class="abs sidebar"></aside>
<div class="abs planner-title">YOUR FLIGHT PLANNER</div>
<div class="abs trip"><span><i class="radio on"></i>One Way</span><span><i class="radio"></i>Round Trip</span></div>
<div class="abs label" style="left:172px;top:231px">Leaving From:</div>
<div class="abs field" style="left:172px;top:245px;width:182px">Enter City or Airport Code</div>
<div class="abs label" style="left:172px;top:278px">Going To:</div>
<div class="abs field" style="left:172px;top:292px;width:182px">Enter City or Airport Code</div>
<div class="abs label" style="left:172px;top:324px">Departure Date and Time:</div>
<div class="abs field" style="left:172px;top:338px;width:90px">mm/dd/yyyy</div>
<div class="abs select" style="left:265px;top:338px;width:87px"><span>12:00am</span><i>▾</i></div>
<div class="abs label" style="left:172px;top:370px">Return Date and Time:</div>
<div class="abs field" style="left:172px;top:385px;width:90px">mm/dd/yyyy</div>
<div class="abs select" style="left:265px;top:385px;width:87px"><span>12:00am</span><i>▾</i></div>
<div class="abs label" style="left:176px;top:419px">Passengers:</div>
<div class="abs field" style="left:176px;top:434px;width:99px"># of passangers</div>
<div class="abs btn-question">QUESTION?</div>
<div class="abs btn-go">GO</div>
<div class="abs contact-card" role="img" aria-label="Support agent with headset photo"><span>Contact Us</span></div>

<div class="abs hero" role="img" aria-label="Private jet flying above clouds"></div>
<div class="abs hero-band"></div>
<div class="abs hero-title">AIRLINES ON DEMAND</div>

<div class="abs divider"></div>
<div class="abs content"></div>

<div class="abs col-head" style="left:385px;top:429px">FROM OUR PRESIDENT</div>
<p class="abs quote" style="left:394px;top:457px">"It is a long established fact that a reader will be distracted by the reada-ble content of a page when looking at its layout. The point of using Lorem Ipsum is that it has a more-or-less normal distribution of letters."</p>
<div class="abs signature">Mr. Aldren</div>
<div class="abs pill" style="left:494px;top:617px;width:78px">READ MORE</div>
<div class="abs vline"></div>

<div class="abs col-head" style="left:598px;top:429px">OUR CLIENTS</div>
<p class="abs quote" style="left:599px;top:457px">"It is a long established fact that a reader will be distracted by the reada-ble content of a page when looking at its layout. The point of using Lorem normal distribution of letters."</p>
<div class="abs pill" style="left:723px;top:554px;width:77px">READ MORE</div>
<a class="abs video-link">See Our Air Charter Videos</a>

<div class="abs col-head" style="left:815px;top:429px">AIRCRAFT GALLERYV</div>
<div class="abs gallery" role="img" aria-label="Private jet over deep blue sea"></div>
<div class="abs pill" style="left:938px;top:581px;width:78px">VIEW NOW</div>

<div class="abs social"><span>Journal</span><span>Updates</span><span>Community</span></div>

<div class="abs countries">
India | Australia | Bahrain | Bangladesh | Belgium | Belgique | België | Canada | China | &nbsp; | Europe - English | Europe - French | Europe - Dutch<br>
Hong Kong | &nbsp; | Japan | Kenya | Kuwait | Malaysia | Mauritius | Nepal | New Zealand | Oman | Philippines | Qatar | Singapore | Sri Lanka<br>
Saudi Arabia | South Africa | Switzerland | Thailand | United Arab Emirates | United Kingdom | United States of America
</div>
<div class="abs copy">©2010 COBALT SKYWAY. All Rights Reserved</div>
</body>
</html>
```